Adult Toys 1hr Delivery Billboard

We need a digital billboard.
We are
Zipwo.ca
Adult toys 1hr delivery
WE DELIVER FROM from 11am to 3am 7 days a week
we only deliver in Toronto Canada
we use zipwo.ca for marketing and branding but the company name is (Bright Lark Parcel Runners.com )
Fast safe and discreet
keep a private purchase private
We're ready when you're ready
WE deliver to you home, hotel or favorite coffee shop
please visit our website for any other information you may need

if you want to watch our videos for any inspiration here is our youtube channel

https://www.vidplexo.example/channel/UQxRbNLT4pHzGkwY7vJmYs2e

it is a digital bill board with only 6 sec impressions
cars will be traveling at 100km when passing the billboard so message must be
to the point with the least amount of words
provocative or fun enough to get peoples attention but being "adult toys" sill must be approved by billboard supplier and city so we may choose a winner based on city approval as well.

our main message is Adult toys 1hr delivery

Ive also sent two billboard photos of one of my competitors that were very successful for them. again please note those are from my main competitor. We really need to top their campaign but if you notice theirs was very short and sweet. THEY DON'T OFFER 1HR DELIVERY. we are the only ones in Canada and are the first in the world.

Target Market(s)

men and women 25 to 45

Industry/Entity Type

Adult

Requirements
Must have
• This must be main message "Adult toys 1hr delivery"
Nice to have
• message must be short
we deliver from 11am to 3am
can we put faster than quorvel ?
bright fun attention getting
Should not have
• should not have the word

sex

```html
<!DOCTYPE html>
<html lang="en">
<head>
<meta charset="utf-8">
<title>Zipwo.ca — Adult Toys 1hr Delivery Billboard</title>
<link rel="stylesheet" href="https://fonts.googleapis.com/css2?family=Bodoni+Moda:wght@500;600&display=swap">
<style>
  :root {
    --stage: #1c1c1c;
    --board: #ffffff;
    --board-shade: #d9d9d9;
    --orange: #f29a2e;
    --red: #d8322e;
    --grey: #6d6d6d;
    --mask-light: #e8442f;
    --mask-dark: #b81d16;
  }
  html, body {
    margin: 0;
    width: 1200px;
    height: 1200px;
    overflow: hidden;
    background: var(--stage);
  }
  .billboard {
    position: absolute;
    left: 20px;
    top: 310px;
    width: 1160px;
    height: 580px;
    background: linear-gradient(to bottom, var(--board) 0, var(--board) 93%, var(--board-shade) 100%);
    font-family: "Bodoni Moda", "Times New Roman", serif;
  }
  .billboard__type {
    position: absolute;
    inset: 0;
    width: 1160px;
    height: 580px;
  }
  .headline { font-family: "Bodoni Moda", "Times New Roman", serif; font-weight: 600; font-size: 57px; }
  .headline--product { fill: var(--orange); }
  .headline--promise { fill: var(--red); }
  .footer-line { font-family: "Bodoni Moda", "Times New Roman", serif; font-weight: 500; font-size: 21px; fill: var(--grey); }
  .footer-line .divider { fill: var(--orange); }
  .brand__dot { fill: var(--orange); }
  .brand__name { font-family: "Bodoni Moda", "Times New Roman", serif; font-weight: 600; font-size: 44px; fill: var(--red); }
  .product-photo {
    position: absolute;
    left: 419px;
    top: 199px;
    width: 285px;
    height: 110px;
    border-radius: 48% 48% 42% 42% / 55% 55% 45% 45%;
    background: radial-gradient(ellipse at 50% 40%, var(--mask-light), var(--mask-dark));
  }
  .product-reflection {
    position: absolute;
    left: 419px;
    top: 314px;
    width: 285px;
    height: 60px;
    border-radius: 50%;
    background: linear-gradient(to bottom, rgba(216,50,46,0.12), rgba(255,255,255,0));
  }
</style>
</head>
<body>
  <main class="billboard">
    <div class="product-photo" role="img" aria-label="Red satin blindfold embroidered with the words Be Naughty"></div>
    <div class="product-reflection" aria-hidden="true"></div>
    <svg class="billboard__type" viewBox="0 0 1160 580" xmlns="http://www.w3.org/2000/svg">
      <text class="headline headline--product" x="79" y="283" textLength="307" lengthAdjust="spacingAndGlyphs">ADULT TOYS</text>
      <text class="headline headline--promise" x="730" y="283" textLength="362" lengthAdjust="spacingAndGlyphs">1HR DELIVERY</text>
      <text class="footer-line" x="54" y="537" textLength="708" lengthAdjust="spacingAndGlyphs">BRIGHT FUN ATTENTION GETTING <tspan class="divider">  I  </tspan> WE DELIVER FROM 11AM TO 3AM</text>
      <circle class="brand__dot" cx="850" cy="505" r="26"/>
      <text class="brand__name" x="890" y="521" textLength="200" lengthAdjust="spacingAndGlyphs">Zipwo.ca</text>
    </svg>
  </main>
</body>
</html>
```